Business Card Design Project

We need a business card for a new technology services company. We develop software and implement software packages for our business customers and although we will begin with just one or two service offerings, our service offerings will expand over time. Our name comes from the an author, RK Bellowes, and his "idea" was that opportunity should be based on ability and achievement, not on social status.

We would like to see a design that is standard in its size and shape, but stands apart in its dramatic color contrasts. The card should not use too many colors - the colors used in the background should highlight the brilliant blues of the logo (see attachment) to dramatic effect. The background should not be white.

If necessary, you can change the color of the words "RK Bellowes", but not the word "Idea".

Card size should be U.S. standard 2 inches by 3.5 inches and provide for 1/8 inch bleed area on each side.

We need a design for both sides of the business card, one side communicating the company logo and contact information, the other side being purely graphical, incorporating the logo but no other information.

Contact Information Required:
Mark Linden
MarkLinden@rkbellowesidea.com
555-304-7812

Target Market(s)

Business executives

Industry/Entity Type

Software

Requirements
Must have
• It must have the full company logo on one side, and at least the graphic element of the logo on the other. Either that or the full logo on both.
Nice to have
• It would be nice to have a design that could work without needing two different textures. For example, it would be nice if the entire card could be shiny, not just parts of the card.

It would also be nice if texture is something we could add later.
Should not have
• The card should not use the color green.

```html
<!DOCTYPE html>
<html lang="en">
<head>
<meta charset="utf-8">
<title>Corvane Labs — Business Card</title>
<link rel="stylesheet" href="https://fonts.googleapis.com/css2?family=Cabin:wght@400;500&display=swap">
<style>
  :root {
    --page-bg: #3b3d40;
    --card-deep: #0b1220;
    --card-mid: #141d2e;
    --brand-blue: #1b9ad8;
    --dot-blue: #1d4d70;
    --dot-blue-soft: #163a57;
    --text-light: #c8ced6;
  }
  * { box-sizing: border-box; margin: 0; padding: 0; }
  html, body {
    width: 1200px;
    height: 900px;
    overflow: hidden;
    background: var(--page-bg);
    font-family: "Cabin", sans-serif;
  }
  .sheet {
    width: 1200px;
    height: 900px;
    display: flex;
    flex-direction: column;
    align-items: center;
    justify-content: center;
    gap: 24px;
  }
  .card {
    position: relative;
    width: 735px;
    height: 420px;
    overflow: hidden;
    background: radial-gradient(ellipse at 40% 45%, var(--card-mid) 0%, var(--card-deep) 75%);
    box-shadow: 0 10px 30px rgba(0,0,0,.45);
  }
  .dot-field {
    position: absolute;
    border-radius: 50%;
    opacity: .75;
  }
  .card-back .dot-field {
    right: -60px;
    top: -40px;
    width: 380px;
    height: 500px;
    background: radial-gradient(ellipse at 60% 50%, var(--dot-blue) 0%, var(--dot-blue-soft) 45%, rgba(22,58,87,0) 72%);
  }
  .card-front .dot-field {
    left: -60px;
    top: -70px;
    width: 380px;
    height: 300px;
    background: radial-gradient(ellipse at 40% 45%, var(--dot-blue) 0%, var(--dot-blue-soft) 45%, rgba(22,58,87,0) 72%);
  }
  .brand {
    position: absolute;
    display: flex;
    align-items: center;
    gap: 18px;
    color: var(--brand-blue);
    font-weight: 400;
    white-space: nowrap;
  }
  .brand-mark {
    width: 46px;
    height: 46px;
    border-radius: 50%;
    background: var(--brand-blue);
    flex: none;
  }
  .card-back .brand {
    left: 60px;
    top: 172px;
    font-size: 40px;
  }
  .card-front .brand {
    right: 48px;
    top: 168px;
    font-size: 36px;
  }
  .contact {
    position: absolute;
    right: 110px;
    top: 262px;
    text-align: right;
    color: var(--text-light);
    font-size: 17px;
    line-height: 1.35;
    white-space: nowrap;
  }
  .contact-name {
    color: var(--brand-blue);
    font-size: 24px;
    font-weight: 500;
    letter-spacing: 1px;
    text-transform: uppercase;
    margin-bottom: 6px;
  }
</style>
</head>
<body>
  <main class="sheet">
    <section class="card card-back" aria-label="Card back">
      <div class="dot-field" role="img" aria-label="Cluster of translucent blue dots"></div>
      <div class="brand">
        <span class="brand-name">Corvane Labs</span>
        <span class="brand-mark"></span>
      </div>
    </section>

    <section class="card card-front" aria-label="Card front">
      <div class="dot-field" role="img" aria-label="Cluster of translucent blue dots"></div>
      <div class="brand">
        <span class="brand-name">Corvane Labs</span>
        <span class="brand-mark"></span>
      </div>
      <div class="contact">
        <p class="contact-name">Mark Linden</p>
        <p class="contact-email">MarkLinden@rkbellowesidea.com</p>
        <p class="contact-phone">555-304-7812</p>
      </div>
    </section>
  </main>
</body>
</html>
```